Modern Website Design for PollMeridian – CX & Loyalty SaaS Platform

We need a modern, professional, and responsive website design for our B2B SaaS platform, PollMeridian. We help companies collect real-time customer feedback, analyze insights, and improve loyalty — combining a powerful CX platform with expert consulting services. The website should clearly communicate who we are and what we offer within the first impression. It should balance data-driven visuals such as dashboards, analytics, and charts with a human, approachable feel. The design must include at least six key pages: Homepage, Product/Services, About, Blog/Resources, Contact/Demo, and Pricing. It should be conversion-focused with clear calls-to-action that encourage visitors to request a demo or contact us. The site must be fully responsive across desktop, tablet, and mobile. It should support multiple languages, starting with English and Danish. Most importantly, the delivery must be a final WordPress website, ready to go live, not just design files.

Target Market(s)

Our target market is medium-to-large B2B organizations. The primary audience includes CX leaders, executives, and managers in customer success and service who want to measure loyalty, understand customer insights, and improve retention.

Industry/Entity Type

Technology / SaaS / Customer Experience

Coding

Coded - Design and coding required

Number of Pages Required

5+ page

Font styles to use
Sans Serif

Requirements
Must have
• The project must deliver a final WordPress website that is fully responsive across all devices. The design should be clean, modern, and SaaS-inspired, with clear calls-to-action on every page. It must also support English and Danish, with a visible language toggle. The site should include visuals of dashboards and analytics that reflect data-driven insights. It must feature sections for case studies or testimonials to build trust. The copywriting should be SEO-friendly, and the design should include smooth animations or hover effects that add polish without making the website feel heavy.
Should not have
• Cluttered layouts, or generic stock photos such as handshakes

```html
<!DOCTYPE html>
<html lang="en">
<head>
<meta charset="utf-8">
<title>PollMeridian – CX &amp; Loyalty Platform</title>
<link href="https://fonts.googleapis.com/css2?family=Lexend:wght@400;500;600;700&family=Poppins:wght@300;400;500;600&display=swap" rel="stylesheet">
<style>
:root{
  --blue:#2456a6;
  --blue-dark:#1c4589;
  --navy:#14213d;
  --orange:#e8542a;
  --grey:#7a8190;
  --white:#ffffff;
}
*{box-sizing:border-box;margin:0;padding:0}
html,body{width:1200px;height:4580px;overflow:hidden}
body{position:relative;font-family:"Poppins",sans-serif;color:var(--navy);background:var(--white)}
a{text-decoration:none;color:inherit}
.abs{position:absolute}
h1,h2,h3,h4,.brand{font-family:"Lexend",sans-serif}
.brand{font-weight:600;color:var(--blue);font-size:26px;display:flex;align-items:center;gap:8px;white-space:nowrap}
.brand::before{content:"";width:14px;height:14px;background:var(--orange);border-radius:50%;flex:none}
.btn{display:flex;align-items:center;justify-content:center;font-size:12px;font-weight:500;border-radius:4px}
.btn-primary{background:var(--blue);color:var(--white)}
.btn-outline{border:1.5px solid var(--blue);color:var(--navy);background:var(--white)}
.eyebrow{font-family:"Lexend",sans-serif;font-weight:500;font-size:15px;text-align:center;width:1200px;left:0}
.section-title{font-family:"Lexend",sans-serif;font-weight:500;font-size:29px;text-align:center;width:1200px;left:0;line-height:1.25}
.tick{display:inline-flex;width:15px;height:15px;border-radius:50%;background:var(--orange);align-items:center;justify-content:center;flex:none}
.tick svg{width:9px;height:9px}
.media{border-radius:10px}

.hero{left:0;top:0;width:1200px;height:925px;background:linear-gradient(180deg,#8db5e6 0%,#b9d2f0 45%,#e4eef9 78%,#ffffff 100%)}
.nav-link{font-size:13px;font-weight:500;color:var(--navy);top:55px}
.hero-title{left:0;width:1200px;top:150px;text-align:center;color:var(--white);font-size:54px;font-weight:600;letter-spacing:2px;line-height:70px;text-transform:uppercase}
.laptop{left:190px;top:382px;width:820px;height:508px;border-radius:16px 16px 30px 30px;background:linear-gradient(180deg,#2a2d33 0%,#e9edf3 8%,#f3f5f9 70%,#c9ccd2 90%,#9a9ea6 100%)}

.diamond{left:156px;top:1022px;width:431px;height:427px;clip-path:polygon(50% 0,100% 50%,50% 100%,0 50%);background:linear-gradient(135deg,#d9dde3 0%,#8c5a4a 50%,#3d4a5c 100%)}
.about-copy{left:612px;top:1050px;width:448px}
.about-copy p{font-size:9px;line-height:20px;color:var(--grey)}
.check-row{display:flex;align-items:center;gap:8px;font-size:11.5px;margin-top:8px;white-space:nowrap}
.progress{height:5px;background:#e2e5ea;border-radius:3px;margin-top:6px}
.progress span{display:block;height:100%;width:95%;background:var(--navy);border-radius:3px}

.services{left:0;top:1552px;width:1200px;height:676px;background:linear-gradient(180deg,#7fa8e0 0%,#a8c7ee 55%,#8bb2e5 100%)}
.service-card{top:199px;width:441px;height:420px;background:var(--white);border-radius:12px}
.service-card h3{position:absolute;left:19px;top:18px;font-size:25px;font-weight:500}
.service-card ul{position:absolute;left:19px;top:70px;list-style:none;font-size:10.5px;color:#333}
.service-card li{margin-bottom:14px;display:flex;align-items:center;gap:8px}
.service-card li::before{content:"";width:5px;height:5px;background:var(--navy);border-radius:50%}
.service-card .brand{position:absolute;right:24px;top:100px;font-size:20px}
.service-card .media{position:absolute;left:18px;top:192px;width:405px;height:208px}

.price-card{width:292px;background:var(--white);border:1px solid #e3e6eb;border-radius:12px;box-shadow:0 4px 14px rgba(20,33,61,.12);padding:30px 20px 0}
.price-card.featured{background:var(--blue);color:var(--white);border:none}
.plan{font-size:12px;font-weight:500}
.price-row{display:flex;align-items:center;gap:18px;margin-top:2px}
.amount{font-family:"Lexend",sans-serif;font-size:60px;font-weight:500;line-height:70px}
.per{font-size:12px;line-height:16px}
.price-desc{font-size:11.5px;margin-top:14px}
.price-card .btn{height:32px;margin-top:14px;font-size:12px}
.price-card .btn+.btn{margin-top:10px}
.featured .btn-primary{background:var(--white);color:var(--navy)}
.featured .btn-outline{background:transparent;border-color:var(--white);color:var(--white)}
.features{font-size:12px;font-weight:500;margin-top:26px}
.feature-note{font-size:9px;margin-top:14px}
.featured .tick{background:var(--white)}

.blog-card{top:3076px;width:213px;height:302px;background:var(--white);border-radius:10px;overflow:hidden}
.blog-card.raised{box-shadow:0 4px 14px rgba(20,33,61,.15)}
.blog-card .media{width:213px;height:199px;border-radius:10px 10px 0 0}
.blog-card .date{font-size:9px;color:var(--grey);margin:14px 9px 0}
.blog-card h4{font-size:13.5px;font-weight:600;margin:6px 9px 0;white-space:nowrap}
.blog-card p{font-size:9.6px;line-height:19px;color:var(--grey);margin:6px 9px 0;white-space:nowrap}

.contact-box{left:151px;top:3584px;width:900px;height:526px;background:var(--white);border-radius:10px;box-shadow:0 3px 14px rgba(20,33,61,.14)}
.field-label{left:510px;font-size:12px;color:var(--grey)}
.field{left:505px;width:502px;height:42px;border:1px solid #c4c8cf;border-radius:10px}

.footer{left:0;top:4205px;width:1200px;height:375px;background:linear-gradient(180deg,#86ade3 0%,#a7c5ec 100%)}
.footer h4{font-size:18px;font-weight:500}
.footer-link{font-size:11.5px}
.social{width:20px;height:20px;border-radius:50%;background:var(--orange)}
</style>
</head>
<body>

<section class="hero abs">
  <div class="brand abs" style="left:151px;top:60px">PollMeridian</div>
  <a class="nav-link abs" style="left:400px">Home</a>
  <a class="nav-link abs" style="left:487px">About Us</a>
  <a class="nav-link abs" style="left:592px">Services</a>
  <a class="nav-link abs" style="left:694px">Blog</a>
  <a class="nav-link abs" style="left:771px">Pricing</a>
  <a class="btn abs" style="left:960px;top:48px;width:91px;height:32px;background:var(--white);color:var(--navy);font-size:9px">Contact Us</a>
  <h1 class="hero-title abs">Turn Customer Feedback<br>Into Loyalty &amp; Growth</h1>
  <a class="btn btn-primary abs" style="left:543px;top:316px;width:114px;height:33px;font-size:9.5px">Request A Demo</a>
  <div class="laptop abs" role="img" aria-label="Laptop showing the analytics dashboard with order, revenue and user charts"></div>
</section>

<section>
  <div class="diamond abs" role="img" aria-label="Diamond photo collage of a team member seated in a bright office"></div>
  <div class="about-copy abs">
    <div style="font-family:Lexend,sans-serif;font-weight:500;font-size:15px">About Us</div>
    <h2 style="font-size:29px;font-weight:500;line-height:36px;margin-top:8px">Your Partner In Customer<br>Experience Excellence</h2>
    <p style="margin-top:18px">We Are More Than Just A Business — We Are A Dedicated Team Of Professionals Passionate About Delivering Exceptional.We Are More Than Just A Business — We Are A Dedicated Team Of Professionals Passionate About Delivering Exceptional.We Are More Than Just A Business — We Are A Dedicated Team Of Professionals Ptional.</p>
    <div class="check-row" style="margin-top:18px"><span class="tick"><svg viewBox="0 0 10 10"><path d="M2 5.2l2 2 4-4.4" stroke="#fff" stroke-width="1.6" fill="none"/></svg></span>We Are More Than Just A Business — We Are A Dedicated</div>
    <div class="check-row"><span class="tick"><svg viewBox="0 0 10 10"><path d="M2 5.2l2 2 4-4.4" stroke="#fff" stroke-width="1.6" fill="none"/></svg></span>Professionals Passionate About Delivering Exceptional.</div>
    <div style="display:flex;justify-content:space-between;width:392px;margin-top:26px;font-size:12px;font-weight:500"><span>Experience</span><span>95%</span></div>
    <div class="progress" style="width:392px"><span></span></div>
    <a class="btn btn-primary" style="width:114px;height:34px;margin-top:24px;font-size:11.5px">Learn More</a>
  </div>
</section>

<section class="services abs">
  <div class="eyebrow abs" style="top:52px">Services</div>
  <h2 class="section-title abs" style="top:80px">Powerful CX Tools, Backed By<br>Expert Guidance</h2>
  <div class="service-card abs" style="left:151px">
    <h3>SaaS Platform</h3>
    <ul><li>Real-Time Feedback Collection</li><li>Analytics &amp; Dashboards</li><li>Customer Insights</li><li>Retention &amp; Loyalty Measurement</li></ul>
    <div class="brand">PollMeridian</div>
    <div class="media" role="img" aria-label="Server room with a cloud SaaS badge" style="background:linear-gradient(135deg,#1b3f7a,#4b86c9 60%,#9cc3ea)"></div>
  </div>
  <div class="service-card abs" style="left:610px">
    <h3>Consulting Services</h3>
    <ul><li>CX Strategy Consulting</li><li>Data Interpretation &amp; Insights</li><li>Loyalty &amp; Retention Programs</li><li>Best Practice Implementation</li></ul>
    <div class="brand">PollMeridian</div>
    <div class="media" role="img" aria-label="Consultants meeting in a glass-walled office" style="background:linear-gradient(135deg,#34475f,#8aa3bf 55%,#cfdbe8)"></div>
  </div>
</section>

<section>
  <div class="eyebrow abs" style="top:2317px">Pricing</div>
  <h2 class="section-title abs" style="top:2340px">Simple, Transparent Plans Designed To Grow With You</h2>

  <div class="price-card abs" style="left:151px;top:2500px;height:373px">
    <div class="plan">Basic Plan</div>
    <div class="price-row"><span class="amount">$10</span><span class="per">Per User<br>Per Month</span></div>
    <div class="price-desc">Basic Featuchers For Up To 10 User.</div>
    <a class="btn btn-primary">Get Started</a>
    <a class="btn btn-outline">Chat To Sales</a>
    <div class="features">FEATURES</div>
    <div class="feature-note">Basic Featuchers For Up To 10 User.</div>
    <div class="check-row" style="font-size:11px;margin-top:10px"><span class="tick"><svg viewBox="0 0 10 10"><path d="M2 5.2l2 2 4-4.4" stroke="#fff" stroke-width="1.6" fill="none"/></svg></span>Lorem Ipsum Dolor Sit,</div>
    <div class="check-row" style="font-size:11px"><span class="tick"><svg viewBox="0 0 10 10"><path d="M2 5.2l2 2 4-4.4" stroke="#fff" stroke-width="1.6" fill="none"/></svg></span>Lorem Ipsum Dolor Sit Amet,</div>
  </div>

  <div class="price-card featured abs" style="left:455px;top:2430px;height:374px">
    <div class="plan">Basic Plan</div>
    <div class="price-row"><span class="amount">$10</span><span class="per">Per User<br>Per Month</span></div>
    <div class="price-desc">Basic Featuchers For Up To 10 User.</div>
    <a class="btn btn-primary">Get Started</a>
    <a class="btn btn-outline">Chat To Sales</a>
    <div class="features">FEATURES</div>
    <div class="feature-note">Basic Featuchers For Up To 10 User.</div>
    <div class="check-row" style="font-size:11px;margin-top:10px"><span class="tick"><svg viewBox="0 0 10 10"><path d="M2 5.2l2 2 4-4.4" stroke="#2456a6" stroke-width="1.6" fill="none"/></svg></span>Lorem Ipsum Dolor Sit,</div>
    <div class="check-row" style="font-size:11px"><span class="tick"><svg viewBox="0 0 10 10"><path d="M2 5.2l2 2 4-4.4" stroke="#2456a6" stroke-width="1.6" fill="none"/></svg></span>Lorem Ipsum Dolor Sit Amet,</div>
  </div>

  <div class="price-card abs" style="left:759px;top:2500px;height:373px">
    <div class="plan">Basic Plan</div>
    <div class="price-row"><span class="amount">$10</span><span class="per">Per User<br>Per Month</span></div>
    <div class="price-desc">Basic Featuchers For Up To 10 User.</div>
    <a class="btn btn-primary">Get Started</a>
    <a class="btn btn-outline">Chat To Sales</a>
    <div class="features">FEATURES</div>
    <div class="feature-note">Basic Featuchers For Up To 10 User.</div>
    <div class="check-row" style="font-size:11px;margin-top:10px"><span class="tick"><svg viewBox="0 0 10 10"><path d="M2 5.2l2 2 4-4.4" stroke="#fff" stroke-width="1.6" fill="none"/></svg></span>Lorem Ipsum Dolor Sit,</div>
    <div class="check-row" style="font-size:11px"><span class="tick"><svg viewBox="0 0 10 10"><path d="M2 5.2l2 2 4-4.4" stroke="#fff" stroke-width="1.6" fill="none"/></svg></span>Lorem Ipsum Dolor Sit Amet,</div>
  </div>
</section>

<section>
  <div class="eyebrow abs" style="top:2963px">Blog</div>
  <h2 class="section-title abs" style="top:2986px">Expert Insights To Elevate Your Customer Experience</h2>
  <article class="blog-card abs" style="left:151px">
    <div class="media" role="img" aria-label="Team discussing customer insights" style="background:linear-gradient(135deg,#e8e6e2,#a0523f 60%,#4d4f59)"></div>
    <div class="date">February 15,2024</div><h4>Customer Insights</h4>
    <p>Lorem Ipsum Dolor Sit Amet<br>Consectetur. Nam Ac</p>
  </article>
  <article class="blog-card abs" style="left:380px">
    <div class="media" role="img" aria-label="Colleagues at a strategy workshop" style="background:linear-gradient(135deg,#5b6a7c,#b04236 55%,#d9d3cc)"></div>
    <div class="date">January 23,2024</div><h4>CX Strategy Consulting</h4>
    <p>Lorem Ipsum Dolor Sit Amet<br>Consectetur. Nam Ac Ornare Sit</p>
  </article>
  <article class="blog-card raised abs" style="left:608px">
    <div class="media" role="img" aria-label="Monitor showing data charts on a desk" style="background:linear-gradient(135deg,#2c4f7d,#6ea0d6 55%,#c7d8ea)"></div>
    <div class="date">February 29,2023</div><h4>Data Interpretation</h4>
    <p>Lorem Ipsum Dolor Sit &nbsp;Consectetur.<br>Nam Ac Ornare Sit Enim Sem.</p>
  </article>
  <article class="blog-card abs" style="left:836px">
    <div class="media" role="img" aria-label="Hands joining puzzle gear pieces" style="background:linear-gradient(135deg,#e9ecf0,#b4875c 55%,#6e5a48)"></div>
    <div class="date">March 26,2024</div><h4>Practice Implementation</h4>
    <p>Lorem Ipsum Dolor Sit Amet<br>Consectetur. Nam</p>
  </article>
</section>

<section>
  <div class="eyebrow abs" style="top:3473px">Contact Us</div>
  <h2 class="section-title abs" style="top:3497px">Let’s Talk CX</h2>
  <div class="contact-box abs"></div>
  <div class="abs" role="img" aria-label="Analysts working at monitors in a data centre" style="left:151px;top:3584px;width:311px;height:526px;border-radius:10px 0 0 10px;background:linear-gradient(160deg,#1d2a3c,#2f5e8e 55%,#0f1826)"></div>
  <h3 class="abs" style="left:503px;top:3628px;font-size:29px;font-weight:400">Contact Us</h3>
  <label class="field-label abs" style="top:3684px">Name</label>
  <div class="field abs" style="top:3712px"></div>
  <label class="field-label abs" style="top:3767px">Email</label>
  <div class="field abs" style="top:3797px"></div>
  <label class="field-label abs" style="top:3852px">Addess</label>
  <div class="field abs" style="top:3883px"></div>
  <label class="field-label abs" style="top:3933px">Phone Number</label>
  <div class="field abs" style="top:3963px"></div>
  <a class="btn btn-primary abs" style="left:503px;top:4032px;width:504px;height:34px">Submit</a>
</section>

<footer class="footer abs">
  <div class="brand abs" style="left:151px;top:80px;font-size:28px">PollMeridian</div>
  <p class="abs" style="left:151px;top:188px;font-size:11px;line-height:19px">Lorem Ipsum Dolor Amet Consectetur.<br>Mauris Enim Dapibus Mauris Leo</p>
  <div class="abs" style="left:151px;top:240px;display:flex;gap:15px">
    <span class="social"></span><span class="social"></span><span class="social"></span><span class="social"></span>
  </div>
  <h4 class="abs" style="left:761px;top:88px">Services</h4>
  <a class="footer-link abs" style="left:768px;top:137px">Plumber</a>
  <a class="footer-link abs" style="left:768px;top:173px">Heating</a>
  <a class="footer-link abs" style="left:768px;top:207px">Drains</a>
  <h4 class="abs" style="left:969px;top:99px">Legal</h4>
  <a class="footer-link abs" style="left:969px;top:140px">Terms Of Use</a>
  <a class="footer-link abs" style="left:969px;top:173px">Privacy Policy</a>
  <a class="footer-link abs" style="left:969px;top:207px">Cookie Policy</a>
  <div class="abs" style="left:151px;top:323px;width:900px;height:1px;background:var(--navy)"></div>
  <div class="abs" style="left:151px;top:346px;font-size:10px">Copyright © 2025 All Right Reserved</div>
  <div class="abs" style="left:757px;top:346px;font-size:10px;display:flex;gap:30px"><span>Privacy Policy</span><span>Terms Of Service</span><span>Cookies Settings</span></div>
</footer>

</body>
</html>
```